Business Cards Design for the electrical wholesaler: clean bold dynamic :)

We need a business card design that would follow our latest brand guidelines. As an electrical wholesaler we want to bring a fresh look and feel into the industry. The design should be clean bold and dynamic. It should come alive with the renewed energy of our green colour. Our grey colour should keep things balanced and complement the notion of maturity and responsibility. We employ Lato as a corporate font however are not bound by this font and we’re open to interpretation here.

Target Market(s)

Electrical contractors

Industry/Entity Type

Business

Contact Information for Business Card

Logo
Name & Surname: Olena Dovbush
Job Title: Director of Marketing
Email: helen.dovbush@mailvane.example
Cell phone: XXX.XXX.XXXX
Address: 20917 - 87 Ave. Edmonton, AB, Canada. T6K 2R8
Business Phone: 780.555.0187
Website: www.qorvil.example

Font styles to use
Other font styles liked:
• Lato

Requirements
Must have
• Logo & website
Nice to have
• Brand elements - some of them you may find in the attached Brand Guidelines (e.g. three lines on the background signifying "W")

```html
<!DOCTYPE html>
<html lang="en">
<head>
<meta charset="utf-8">
<title>Qorvil Business Cards</title>
<link rel="stylesheet" href="https://fonts.googleapis.com/css2?family=Lato:wght@400;700;900&display=swap">
<style>
  :root {
    --green: #8cc63f;
    --green-deep: #76b82a;
    --grey-dark: #343436;
    --grey-mid: #48484b;
    --ink: #3b3b3d;
    --white: #ffffff;
    --paper: #eeeeee;
    --canvas: #f6f6f6;
  }
  * { box-sizing: border-box; margin: 0; padding: 0; }
  html, body {
    width: 1200px; height: 1200px; overflow: hidden;
    background: var(--canvas);
    font-family: "Lato", sans-serif;
  }
  .sheet {
    width: 1200px; height: 1200px;
    display: flex; align-items: center; justify-content: center; gap: 40px;
  }
  .card {
    position: relative;
    width: 540px; height: 330px;
    overflow: hidden;
    box-shadow: 0 10px 22px rgba(0,0,0,0.35);
  }

  /* Front (contact side) */
  .card--front {
    background: linear-gradient(120deg, var(--grey-mid) 0%, var(--grey-dark) 70%);
    color: var(--white);
  }
  .brand {
    display: flex; align-items: center; gap: 12px;
    font-weight: 700; font-size: 44px; line-height: 1; letter-spacing: 0.5px;
  }
  .brand__mark { width: 26px; height: 26px; background: var(--green); }
  .card--front .brand { position: absolute; left: 30px; top: 26px; color: var(--white); }

  .nameplate {
    position: absolute; left: 304px; top: 127px;
    display: flex; align-items: center; height: 30px;
  }
  .nameplate__slash {
    width: 8px; height: 30px; background: var(--white);
    transform: skewX(-18deg); margin-right: 12px;
  }
  .nameplate__band {
    background: var(--green); height: 30px; width: 240px;
    display: flex; align-items: center; padding-left: 10px;
    font-size: 25px; color: var(--ink); white-space: nowrap;
  }
  .nameplate__first { font-weight: 900; margin-right: 6px; }
  .nameplate__last { font-weight: 400; }
  .job-title {
    position: absolute; left: 372px; top: 166px;
    font-size: 15px; color: var(--white);
  }

  .contacts { position: absolute; left: 20px; top: 183px; list-style: none; }
  .contacts li {
    display: flex; align-items: center; gap: 8px;
    height: 32px; font-size: 16px; color: var(--white);
  }
  .contacts svg { width: 20px; height: 20px; flex: none; }

  /* Back (brand side) */
  .card--back {
    background: linear-gradient(110deg, var(--green) 0%, var(--green) 45%, var(--green-deep) 100%);
  }
  .card--back .brand {
    position: absolute; left: 0; right: 0; top: 128px;
    justify-content: center; color: var(--ink);
  }
  .rule {
    position: absolute; left: 0; right: 0; top: 270px; height: 9px;
    background: linear-gradient(90deg, rgba(52,52,54,0) 0%, var(--grey-dark) 40%, var(--grey-dark) 100%);
  }
  .web {
    position: absolute; left: 0; right: 0; top: 283px;
    text-align: center; font-weight: 700; font-size: 14px;
    letter-spacing: 1px; color: var(--ink);
  }
</style>
</head>
<body>
<main class="sheet">

  <section class="card card--front" aria-label="Business card, contact side">
    <div class="brand"><span class="brand__mark"></span>qorvil</div>

    <div class="nameplate">
      <span class="nameplate__slash"></span>
      <div class="nameplate__band">
        <span class="nameplate__first">Olena</span><span class="nameplate__last">Dovbush</span>
      </div>
    </div>
    <p class="job-title">Director of Marketing</p>

    <ul class="contacts">
      <li>
        <svg viewBox="0 0 20 20" aria-hidden="true"><polygon points="10,1 18,5.5 18,14.5 10,19 2,14.5 2,5.5" fill="#8cc63f"/><path d="M7 5.5 l2 2.5 -1 1.2 c0.8 1.5 1.6 2.3 3 3 l1.2 -1 2.3 2 -1.2 1.5 c-3.2 -0.3 -6.3 -3.4 -6.6 -6.7z" fill="#343436"/></svg>
        780.555.0187
      </li>
      <li>
        <svg viewBox="0 0 20 20" aria-hidden="true"><polygon points="10,1 18,5.5 18,14.5 10,19 2,14.5 2,5.5" fill="#8cc63f"/><rect x="7" y="5" width="6" height="10" rx="1" fill="#343436"/><rect x="8" y="6.3" width="4" height="6.2" fill="#8cc63f"/></svg>
        780.555.0142
      </li>
      <li>
        <svg viewBox="0 0 20 20" aria-hidden="true"><polygon points="10,1 18,5.5 18,14.5 10,19 2,14.5 2,5.5" fill="#8cc63f"/><circle cx="10" cy="10" r="4.5" fill="none" stroke="#343436" stroke-width="1.2"/><path d="M5.5 10 h9 M10 5.5 c-2 3 -2 6 0 9 M10 5.5 c2 3 2 6 0 9" fill="none" stroke="#343436" stroke-width="1"/></svg>
        www.qorvil.example
      </li>
      <li>
        <svg viewBox="0 0 20 20" aria-hidden="true"><polygon points="10,1 18,5.5 18,14.5 10,19 2,14.5 2,5.5" fill="#8cc63f"/><path d="M10 15 c-2.5 -3 -3.5 -4.5 -3.5 -6.2 a3.5 3.5 0 0 1 7 0 c0 1.7 -1 3.2 -3.5 6.2z" fill="#343436"/><circle cx="10" cy="8.7" r="1.3" fill="#8cc63f"/></svg>
        20917 - 87 Ave. Edmonton, AB, Canada. T6K 2R8
      </li>
    </ul>
  </section>

  <section class="card card--back" aria-label="Business card, brand side">
    <div class="brand"><span class="brand__mark"></span>qorvil</div>
    <div class="rule"></div>
    <p class="web">WWW.QORVIL.EXAMPLE</p>
  </section>

</main>
</body>
</html>
```